Outdated Brindlequay.com Website redesign

Brindlequay.com is a construction supply company with 90% delivery of their product to local area builders. Phase one is about improving their online presence, mobile-friendly, and being informative. We are not looking to add any e-commerce abilities in this phase. Please review the documents attached for all the details you need to produce a mock-up. We are also redeveloping their logo (here in DC) but for now, use their old logo asa. place holder.

```html
<!DOCTYPE html>
<html lang="en">
<head>
<meta charset="UTF-8">
<title>Brindlequay Industries Co., Inc.</title>
<link href="https://fonts.googleapis.com/css2?family=Roboto:wght@400;500;700;900&family=Russo+One&display=swap" rel="stylesheet">
<style>
:root{
  --green:#0a7d0a;
  --green-bright:#16e01a;
  --green-mid:#1fa51f;
  --ink:#111111;
  --text:#555555;
  --white:#ffffff;
  --light:#f5f5f5;
  --footer:#1e1e1e;
  --footer-text:#dddddd;
  --asphalt:#3a3835;
  --vest:#e0661c;
}
*{margin:0;padding:0;box-sizing:border-box}
html,body{width:1200px;height:3319px;overflow:hidden;background:var(--white)}
body{font-family:"Roboto",Arial,sans-serif;color:var(--ink)}
.page{position:relative;width:1200px;height:3319px;overflow:hidden}
.abs{position:absolute}

/* header */
.site-header{position:absolute;left:0;top:0;width:1200px;height:78px;background:var(--white)}
.brand{position:absolute;left:168px;top:22px;display:flex;align-items:center;gap:8px;font-weight:700;font-size:24px;color:var(--green);letter-spacing:1px}
.brand-dot{width:14px;height:14px;border-radius:50%;background:var(--green-bright)}
.main-nav{position:absolute;top:32px;font-size:13px;color:#333}
.main-nav span{position:absolute;white-space:nowrap}
.main-nav .active{color:var(--green)}
.phone-box{position:absolute;left:905px;top:16px;width:137px;height:46px;border:1px solid #222;border-radius:0 14px 0 14px;display:flex;align-items:center;justify-content:center;gap:6px;font-weight:700;font-size:15px}

/* hero */
.hero-photo{position:absolute;left:0;top:78px;width:1200px;height:580px;
  background:
    radial-gradient(ellipse 170px 260px at 90px 160px,rgba(224,102,28,.85) 0%,rgba(224,102,28,.35) 55%,transparent 80%),
    radial-gradient(ellipse 150px 240px at 1130px 200px,rgba(224,102,28,.85) 0%,rgba(224,102,28,.35) 55%,transparent 80%),
    radial-gradient(ellipse 130px 200px at 770px 90px,rgba(200,200,200,.35) 0%,transparent 75%),
    radial-gradient(ellipse 90px 200px at 1160px 470px,rgba(40,110,40,.8) 0%,transparent 80%),
    radial-gradient(ellipse 90px 200px at 40px 470px,rgba(40,110,40,.7) 0%,transparent 80%),
    linear-gradient(180deg,#6b6a66 0%,#4a4743 35%,#2f2d2a 70%,#45403a 100%)}
.hero-shade{position:absolute;left:0;top:78px;width:1200px;height:580px;background:radial-gradient(ellipse 420px 300px at 600px 330px,rgba(0,0,0,.35) 0%,rgba(0,0,0,.1) 100%)}
.hero-green{position:absolute;left:0;top:640px;width:1200px;height:183px;background:var(--green)}
.hero-wave{position:absolute;left:0;top:540px}
.hero-title{position:absolute;left:0;width:1200px;text-align:center}
.hero-name{top:255px;font-family:"Russo One",sans-serif;font-size:54px;color:var(--green-bright);letter-spacing:1px}
.hero-sub{top:325px;font-family:"Russo One",sans-serif;font-size:32px;color:var(--green-bright)}
.hero-tag{top:380px;font-size:22px;line-height:32px;color:var(--white)}
.btn-solid{position:absolute;background:var(--green-bright);color:#062e06;font-weight:700;font-size:15px;display:flex;align-items:center;justify-content:center;border-radius:0 14px 0 14px}
.btn-outline{position:absolute;border:1px solid currentColor;font-weight:700;font-size:15px;display:flex;align-items:center;justify-content:center;border-radius:0 16px 0 16px}
.slider-dots{position:absolute;left:1031px;top:322px}
.slider-dots i{display:block;width:10px;height:10px;background:var(--white);margin-bottom:10px}
.slider-dots i.on{background:var(--green-bright)}
.slogan{position:absolute;left:0;top:675px;width:1200px;text-align:center;font-family:"Russo One",sans-serif;font-size:29px;color:var(--white);letter-spacing:1px}

/* about / info */
.photo-card{position:absolute;border-radius:0 90px 0 90px;box-shadow:0 6px 18px rgba(0,0,0,.18);border:6px solid var(--white)}
.section-heading{position:absolute;font-weight:700;font-size:28px;color:var(--ink)}
.body-copy{position:absolute;font-size:14px;line-height:29px;color:var(--text)}

/* why */
.why{position:absolute;left:0;top:1275px;width:1200px;height:497px;
  background:
    radial-gradient(ellipse 200px 260px at 80px 120px,rgba(10,90,10,.55) 0%,transparent 80%),
    radial-gradient(ellipse 180px 260px at 1130px 260px,rgba(10,90,10,.5) 0%,transparent 80%),
    radial-gradient(ellipse 300px 120px at 500px 430px,rgba(10,90,10,.35) 0%,transparent 80%),
    linear-gradient(120deg,#1b8f1b 0%,#23a823 40%,#168516 100%)}
.why-heading{position:absolute;left:158px;top:1350px;font-weight:700;font-size:27px;color:var(--white)}
.why-list{position:absolute;list-style:none;color:var(--white);font-size:15px;font-weight:400;letter-spacing:.4px}
.why-list li{position:absolute;left:0;width:270px;padding-left:22px;line-height:18px;white-space:normal}
.why-list li::before{content:"";position:absolute;left:0;top:4px;width:10px;height:10px;border-radius:50%;background:var(--white)}
.circle-photo{position:absolute;border-radius:50%;border:4px solid var(--white);overflow:hidden;
  background:
    radial-gradient(ellipse 34% 40% at 52% 42%,#6f7a82 0%,#4a5257 60%,transparent 100%),
    radial-gradient(ellipse 30% 18% at 58% 66%,#3b3b3b 0%,transparent 100%),
    linear-gradient(180deg,var(--green-bright) 0%,var(--green-bright) 18%,#9aa39a 32%,#c9cbc6 55%,var(--green-bright) 72%,var(--green-bright) 100%)}

/* partners */
.partners{position:absolute;left:0;top:2178px;width:1200px;height:400px;background:var(--light)}
.partner-badge{position:absolute;top:2325px;width:167px;height:68px;border:1px solid #bbb;background:var(--white);display:flex;align-items:center;justify-content:center}
.partner-badge i{display:block;border-radius:4px}
.pager{position:absolute;top:2429px}
.pager i{position:absolute;width:11px;height:11px;border:1px solid #bbb;background:var(--white)}
.pager i.on{background:var(--green-bright);border-color:var(--green-bright)}

/* newsletter */
.newsletter{position:absolute;left:0;top:2560px;width:1200px;height:315px;background:var(--green)}
.news-field{position:absolute;left:606px;top:2644px;width:392px;height:46px;background:var(--white);font-size:12px;color:#444;padding-left:12px;display:flex;align-items:center}

/* footer */
.site-footer{position:absolute;left:0;top:2875px;width:1200px;height:444px;background:var(--footer);color:var(--footer-text)}
.f-heading{position:absolute;font-weight:700;font-size:16px;color:var(--white)}
.f-text{position:absolute;font-size:12.5px;line-height:24px;color:var(--footer-text)}
.f-icon{position:absolute;width:20px;height:20px;border-radius:50%;background:var(--green-bright);display:flex;align-items:center;justify-content:center}
.f-link{position:absolute;font-size:12.5px;color:var(--green-bright)}
.f-field{position:absolute;height:37px;border:1px solid #888;font-size:12.5px;color:var(--footer-text);padding-left:10px;display:flex;align-items:center}
.social{position:absolute;top:3137px;width:36px;height:36px;border-radius:50%;background:var(--white)}
.f-rule{position:absolute;left:158px;top:3250px;width:884px;height:1px;background:#3a3a3a}
</style>
</head>
<body>
<div class="page">

  <header class="site-header">
    <div class="brand"><span class="brand-dot"></span>BRINDLEQUAY</div>
    <nav class="main-nav">
      <span class="active" style="left:480px">HOME</span>
      <span style="left:554px">ABOUT</span>
      <span style="left:632px">PRODUCTS</span>
      <span style="left:735px">BRANDS</span>
      <span style="left:822px">CONTACT</span>
    </nav>
    <div class="phone-box">
      <svg width="13" height="13" viewBox="0 0 24 24"><path fill="#111" d="M6.6 10.8a15 15 0 0 0 6.6 6.6l2.2-2.2a1 1 0 0 1 1-.25 11.4 11.4 0 0 0 3.6.57 1 1 0 0 1 1 1V20a1 1 0 0 1-1 1A17 17 0 0 1 3 4a1 1 0 0 1 1-1h3.5a1 1 0 0 1 1 1c0 1.25.2 2.45.57 3.57a1 1 0 0 1-.25 1z"/></svg>
      555-014-2288
    </div>
  </header>

  <div class="hero-photo" role="img" aria-label="Road crew in orange safety vests spreading fresh asphalt"></div>
  <div class="hero-shade"></div>
  <div class="hero-green"></div>
  <svg class="hero-wave" width="1200" height="110" viewBox="0 0 1200 110"><path d="M0 15 Q600 181 1200 15 V110 H0Z" fill="#0a7d0a"/></svg>

  <div class="hero-title hero-name">BRINDLEQUAY</div>
  <div class="hero-title hero-sub">INDUSTRIES CO.INC.</div>
  <div class="hero-title hero-tag">Construction Supplies &amp; Building Materials<br>From Our Family To Yours.</div>
  <div class="btn-solid" style="left:521px;top:482px;width:159px;height:50px">CONTACT US</div>
  <div class="slider-dots"><i class="on"></i><i></i><i></i><i></i></div>

  <div class="slogan">WHEN YOU NEED IT NOW, ALL BRINDLEQUAY NOW!</div>
  <div class="btn-outline" style="left:520px;top:736px;width:159px;height:50px;color:var(--white)">VIEW PRODUCTS</div>

  <div class="photo-card" role="img" aria-label="Carpenter in red gloves cutting timber with a circular saw" style="left:160px;top:898px;width:400px;height:312px;background:radial-gradient(ellipse 30% 30% at 45% 30%,#5e6064 0%,transparent 100%),radial-gradient(ellipse 22% 14% at 48% 72%,#d2302a 0%,transparent 100%),radial-gradient(ellipse 40% 30% at 40% 85%,#6a6a6a 0%,transparent 100%),linear-gradient(135deg,#d9a77a 0%,#efe3d2 40%,#f4ece0 70%,#d9c3a2 100%)"></div>
  <h2 class="section-heading" style="left:607px;top:922px">ABOUT</h2>
  <p class="body-copy" style="left:607px;top:968px;width:440px">Brindlequay Industries Co., Inc. is a family owned and operated Wholesale Construction Supply Distributor serving the 5 boroughs of NY and northern NJ. Our knowledge, accuracy, and attention to detail will exceed your expectations with each of your construction and civil supply purchases.</p>
  <div class="btn-outline" style="left:607px;top:1129px;width:150px;height:50px;color:var(--ink)">READ MORE</div>

  <div class="why" role="img" aria-label="Green tinted photo of a road crew at work"></div>
  <h2 class="why-heading">WHY DO BUSINESS WITH BRINDLEQUAY?</h2>
  <ul class="why-list" style="left:158px;top:1434px">
    <li style="top:0">Service and relationship based company</li>
    <li style="top:50px">Deliver fast and on time</li>
    <li style="top:83px">One stop shop with wide range of products</li>
    <li style="top:133px">Knowledgeable sales associates</li>
    <li style="top:167px">Piggy back unloading</li>
    <li style="top:208px">Hours 6am - 5pm in NJ, 6am - 4pm LIC location</li>
  </ul>
  <ul class="why-list" style="left:460px;top:1434px">
    <li style="top:0">Union drivers</li>
    <li style="top:40px">Accurate shipments</li>
    <li style="top:83px">Minimal back orders</li>
    <li style="top:124px">Top name brands</li>
    <li style="top:165px">Reliable &amp; Trustworthy</li>
    <li style="top:208px">Convenient locations</li>
    <li style="top:250px">Competitive Pricing</li>
  </ul>
  <div class="circle-photo" role="img" aria-label="Worker in ear defenders using a power tool" style="left:689px;top:1379px;width:356px;height:356px"></div>

  <h2 class="section-heading" style="left:161px;top:1886px">INFO</h2>
  <p class="body-copy" style="left:161px;top:1932px;width:440px">We focus on supplying construction materials for any size projects including but not limited to bridges, tunnels, highways, airports, water treatment plants &amp; more. With quick and reliable on time delivery, you'll have all the supplies you need to succeed.</p>
  <div class="photo-card" role="img" aria-label="Electrician in safety glasses using a screwdriver on a wall fitting" style="left:640px;top:1813px;width:402px;height:312px;background:radial-gradient(ellipse 25% 35% at 82% 45%,#c79c7e 0%,transparent 100%),radial-gradient(ellipse 25% 20% at 35% 58%,#d9ad90 0%,transparent 100%),radial-gradient(ellipse 12% 12% at 10% 50%,#eeeeea 0%,transparent 100%),linear-gradient(90deg,#5d5550 0%,#7a6258 35%,#8a8580 60%,#a7a39e 100%)"></div>

  <div class="partners"></div>
  <h2 class="section-heading" style="left:0;top:2255px;width:1200px;text-align:center">PARTNERS</h2>
  <div class="partner-badge" style="left:158px"><i style="width:112px;height:24px;background:#cfcfcf"></i></div>
  <div class="partner-badge" style="left:337px"><i style="width:22px;height:22px;border-radius:50%;background:#1f6fb0;margin-right:8px"></i><i style="width:80px;height:24px;background:#b9b9b9"></i></div>
  <div class="partner-badge" style="left:517px"><i style="width:116px;height:20px;background:#6f8fbf"></i></div>
  <div class="partner-badge" style="left:696px"><i style="width:116px;height:22px;background:#d66a5a"></i></div>
  <div class="partner-badge" style="left:875px"><i style="width:96px;height:26px;background:#9a9a9a"></i></div>
  <div class="pager"><i class="on" style="left:969px"></i><i style="left:990px"></i><i style="left:1011px"></i><i style="left:1032px"></i></div>

  <svg class="abs" style="left:0;top:2470px" width="1200" height="100" viewBox="0 0 1200 100"><path d="M0 90 Q600 -74 1200 90 V100 H0Z" fill="#0a7d0a"/></svg>
  <div class="newsletter"></div>
  <div class="circle-photo" role="img" aria-label="Builder leaning over a workbench" style="left:161px;top:2533px;width:310px;height:310px"></div>
  <h2 class="section-heading" style="left:605px;top:2588px;color:var(--white)">SUBSCRIBE NEWSLETTER</h2>
  <div class="news-field">Enter Your Mail ID</div>
  <div class="btn-outline" style="left:606px;top:2705px;width:232px;height:50px;color:var(--white)">SUBSCRIBE NOW</div>

  <footer class="site-footer"></footer>
  <div class="abs" style="left:158px;top:2950px;display:flex;align-items:center;gap:8px;font-weight:700;font-size:22px;color:var(--white);letter-spacing:1px"><span style="width:14px;height:14px;border-radius:50%;background:var(--white)"></span>BRINDLEQUAY</div>
  <p class="f-text" style="left:157px;top:3033px;width:210px">Brindlequay is a family owned and operated company that has been in the business of selling construction supplies since 1991.</p>
  <span class="social" style="left:158px"></span>
  <span class="social" style="left:199px"></span>
  <span class="social" style="left:240px"></span>
  <span class="social" style="left:281px"></span>

  <h3 class="f-heading" style="left:397px;top:2927px">CONTACT INFO</h3>
  <span class="f-icon" style="left:397px;top:2962px"><svg width="10" height="12" viewBox="0 0 24 24"><path fill="#1e1e1e" d="M12 2a7 7 0 0 0-7 7c0 5 7 13 7 13s7-8 7-13a7 7 0 0 0-7-7zm0 9.5A2.5 2.5 0 1 1 12 6.5a2.5 2.5 0 0 1 0 5z"/></svg></span>
  <p class="f-text" style="left:431px;top:2955px;line-height:20px">48 Harlow Lane<br>Westmere, NJ 07000</p>
  <span class="f-icon" style="left:397px;top:3018px"><svg width="10" height="10" viewBox="0 0 24 24"><path fill="#1e1e1e" d="M6.6 10.8a15 15 0 0 0 6.6 6.6l2.2-2.2a1 1 0 0 1 1-.25 11.4 11.4 0 0 0 3.6.57 1 1 0 0 1 1 1V20a1 1 0 0 1-1 1A17 17 0 0 1 3 4a1 1 0 0 1 1-1h3.5a1 1 0 0 1 1 1c0 1.25.2 2.45.57 3.57a1 1 0 0 1-.25 1z"/></svg></span>
  <p class="f-text" style="left:431px;top:3016px">555-014-2288</p>
  <span class="f-icon" style="left:397px;top:3052px"><svg width="10" height="10" viewBox="0 0 24 24"><path fill="#1e1e1e" d="M3 5h18v14H3zm2 2v.5l7 5 7-5V7z"/></svg></span>
  <p class="f-text" style="left:431px;top:3050px">www.brindlequay.com</p>

  <h3 class="f-heading" style="left:397px;top:3105px">QUICK LINK</h3>
  <span class="f-link" style="left:397px;top:3140px">Home</span>
  <span class="f-link" style="left:468px;top:3140px">About</span>
  <span class="f-link" style="left:397px;top:3170px">Products</span>
  <span class="f-link" style="left:485px;top:3170px">Brands</span>
  <span class="f-link" style="left:397px;top:3200px">Contact</span>

  <h3 class="f-heading" style="left:611px;top:2927px">SEND A MESSAGE</h3>
  <div class="f-field" style="left:611px;top:2966px;width:210px">Name</div>
  <div class="f-field" style="left:833px;top:2966px;width:209px">Company</div>
  <div class="f-field" style="left:611px;top:3016px;width:210px">Email</div>
  <div class="f-field" style="left:833px;top:3016px;width:209px">Zipcode</div>
  <div class="f-field" style="left:611px;top:3064px;width:431px">State</div>
  <div class="btn-solid" style="left:611px;top:3113px;width:114px;height:38px;font-size:12px">JOIN NOW</div>
  <p class="f-text" style="left:614px;top:3184px;font-size:12px">Terms &amp; Conditions I &nbsp;Privacy Policy</p>

  <div class="f-rule"></div>
  <p class="f-text" style="left:0;top:3268px;width:1200px;text-align:center;font-size:13px">© 2021 <b style="color:var(--white)">BRINDLEQUAY.</b> All rights reserved.</p>

</div>
</body>
</html>
```